RoadReady Driving School

I need a Facebook page for my Driving School. I teach mostly teenagers how to drive in New Hampshire but also do private classes for adults as well. More info can be found at roadreadylessons.example

```html
<!DOCTYPE html>
<html lang="en">
<head>
<meta charset="utf-8">
<title>RoadReady Driving School – Facebook Cover</title>
<link rel="stylesheet" href="https://fonts.googleapis.com/css2?family=Poppins:wght@500;600;700;800&display=swap">
<style>
  :root {
    --canvas-bg: #ffffff;
    --cover-dark: #1b1b1b;
    --cover-dark-2: #2a2a2a;
    --brand-yellow: #f2c10f;
    --brand-yellow-deep: #c99d07;
    --stripe-grey: #c9c9c9;
    --text-white: #ffffff;
    --rule-grey: #9a9a9a;
  }
  * { margin: 0; padding: 0; box-sizing: border-box; }
  html, body {
    width: 1200px; height: 1124px; overflow: hidden;
    background: var(--canvas-bg);
    font-family: "Poppins", sans-serif;
  }
  .canvas { position: relative; width: 1200px; height: 1124px; }

  .cover {
    position: absolute; left: 0; top: 334px;
    width: 1011px; height: 384px;
    transform: scale(1.18694); transform-origin: top left;
    background: linear-gradient(90deg, var(--cover-dark-2) 0%, var(--cover-dark) 55%, #151515 100%);
    overflow: hidden;
  }
  .cover-shapes { position: absolute; inset: 0; }

  .hero-photo {
    position: absolute; inset: 0;
    clip-path: polygon(0 0, 330px 0, 415px 185px, 350px 384px, 0 384px);
    background: linear-gradient(120deg, #d9dcdf 0%, #8b8e92 35%, #4a4c50 65%, #2c2d30 100%);
  }

  .title {
    position: absolute; left: 483px; top: 28px;
    color: var(--text-white); font-weight: 800;
    font-size: 39px; line-height: 42px; letter-spacing: 0.3px;
  }
  .title-rule {
    position: absolute; left: 483px; top: 125px;
    width: 456px; height: 1.5px; background: var(--rule-grey);
  }
  .title-rule-accent {
    position: absolute; left: 515px; top: 122px;
    width: 108px; height: 6px; border-radius: 3px; background: var(--brand-yellow);
  }
  .tagline-main {
    position: absolute; left: 483px; top: 142px;
    color: var(--brand-yellow); font-weight: 800;
    font-size: 29px; letter-spacing: 0.2px;
  }

  .services {
    position: absolute; left: 485px; top: 192px;
    display: flex; gap: 33px;
  }
  .service { width: 133px; text-align: center; }
  .service-photo {
    width: 133px; height: 78px;
    border: 2px solid var(--brand-yellow);
  }
  .service-photo.teen { background: linear-gradient(135deg, #bcd3e6, #e8c64a 70%, #c79a1a); }
  .service-photo.individual { background: linear-gradient(135deg, #5d6a72, #2e3438 60%, #8b8f93); }
  .service-photo.senior { background: linear-gradient(135deg, #c43a32, #8f2a26 45%, #d8d8d8); }
  .service-label {
    margin-top: 10px;
    color: var(--text-white); font-weight: 500;
    font-size: 12px; line-height: 15px;
  }

  .location-line {
    position: absolute; left: 483px; top: 322px;
    color: var(--text-white); font-weight: 500; font-size: 20px;
  }
  .location-line .brand { color: var(--brand-yellow); font-weight: 700; }
</style>
</head>
<body>
<main class="canvas">
  <section class="cover" aria-label="RoadReady Driving School Facebook cover">
    <div class="hero-photo" role="img" aria-label="Photo of a smiling instructor in glasses at the wheel of a white car giving a thumbs up"></div>

    <svg class="cover-shapes" viewBox="0 0 1011 384" width="1011" height="384" aria-hidden="true">
      <polygon points="360,0 398,0 462,186 402,384 370,384 430,186" fill="var(--stripe-grey)" opacity="0.55"/>
      <polygon points="325,0 360,0 430,186 370,384 340,384 410,186" fill="var(--brand-yellow)"/>
      <polygon points="1011,262 1011,300 983,384 962,384" fill="var(--brand-yellow-deep)"/>
    </svg>

    <h1 class="title">ROADREADY<br>DRIVING SCHOOL</h1>
    <div class="title-rule"></div>
    <div class="title-rule-accent"></div>
    <p class="tagline-main">PREPARING YOU FOR THE ROAD</p>

    <ul class="services" style="list-style:none">
      <li class="service">
        <div class="service-photo teen" role="img" aria-label="Photo of a happy young driver holding up car keys"></div>
        <p class="service-label">TEENAGE GROUP<br>DRIVER EDUCATION</p>
      </li>
      <li class="service">
        <div class="service-photo individual" role="img" aria-label="Photo of an instructor beside a student driver in a car"></div>
        <p class="service-label">INDIVIDUAL<br>DRIVER EDUCATION</p>
      </li>
      <li class="service">
        <div class="service-photo senior" role="img" aria-label="Photo of a senior driver smiling from a red car window"></div>
        <p class="service-label">SENIOR DRIVER<br>EVALUATIONS</p>
      </li>
    </ul>

    <p class="location-line"><span class="brand">RoadReady Driving</span> in Western New Hemisphere</p>
  </section>
</main>
</body>
</html>
```